Bref créative
Quiet Harbor Dental Urgent Clinic- Business Cards and Stationary
Quiet Harbor Dental Urgent Clinic
Professional
Peter Delacroix, Jr., DMD
Founder/ CEO
2718 Pellam Rd
Ste 412
Houston, TX 77291
1-855-GRIN-WELLS
petedx4@mailvane.example
www.GRINWELLS.example
we can see you now!
RED, WHITE AND BLUE
I Have raised the $$$$ for postcard fabrication as well. let's get it!
attached is the graphic concept i'd like to achieve with the postcard.

```html
<!DOCTYPE html>
<html lang="en">
<head>
<meta charset="utf-8">
<title>Quiet Harbor Dental Urgent Clinic – Business Card</title>
<link rel="stylesheet" href="https://fonts.googleapis.com/css2?family=Cinzel:wght@400;600&display=swap">
<style>
  :root {
    --page-bg: #e9e7e3;
    --card-white: #ffffff;
    --brand-blue: #1f5fae;
    --brand-blue-deep: #134689;
    --brand-blue-light: #3a7fd0;
    --brand-red: #d7262e;
    --text-light: #ffffff;
    --text-soft: #dbe7f7;
  }
  * { margin: 0; padding: 0; box-sizing: border-box; }
  html, body {
    width: 1200px; height: 914px; overflow: hidden;
    background: var(--page-bg);
    font-family: "Cinzel", serif;
  }
  .canvas {
    width: 1200px; height: 914px;
    display: flex; align-items: center; justify-content: center;
  }
  .business-card {
    position: relative;
    width: 1050px; height: 600px;
    background: var(--card-white);
    box-shadow: 0 18px 40px rgba(0,0,0,.18);
    overflow: hidden;
  }
  .card-bands { position: absolute; inset: 0; }
  .brand {
    position: absolute; top: 110px; left: 0; width: 100%;
    display: flex; align-items: center; justify-content: center; gap: 20px;
  }
  .brand-dot {
    width: 72px; height: 72px; border-radius: 50%;
    background: var(--brand-blue);
    flex: none;
  }
  .brand-name {
    color: var(--brand-blue);
    font-size: 26px;
    font-weight: 400;
    line-height: 1.3;
    letter-spacing: 1px;
  }
  .identity {
    position: absolute; top: 385px; left: 0; width: 100%;
    text-align: center; color: var(--text-light);
  }
  .identity .person-name { font-size: 24px; font-weight: 600; letter-spacing: 1px; }
  .identity .person-title { font-size: 15px; color: var(--text-soft); margin-top: 4px; letter-spacing: 1px; }
  .address {
    position: absolute; top: 468px; left: 150px;
    font-style: normal;
    color: var(--text-light); font-size: 17px; line-height: 1.6; letter-spacing: .5px;
  }
  .divider {
    position: absolute; top: 462px; left: 520px; width: 1px; height: 100px;
    background: rgba(255,255,255,.5);
  }
  .contacts {
    position: absolute; top: 462px; left: 555px;
    list-style: none; color: var(--text-light);
    font-size: 16px; letter-spacing: .5px;
  }
  .contacts li { display: flex; align-items: center; gap: 12px; height: 34px; }
  .contact-icon {
    width: 24px; height: 24px; border-radius: 50%;
    background: var(--text-light);
    display: flex; align-items: center; justify-content: center; flex: none;
  }
  .contact-icon svg { width: 14px; height: 14px; }
</style>
</head>
<body>
<main class="canvas">
  <section class="business-card">
    <svg class="card-bands" viewBox="0 0 1050 600" preserveAspectRatio="none" aria-hidden="true">
      <defs>
        <linearGradient id="blueBand" x1="0" y1="0" x2="0" y2="1">
          <stop offset="0" stop-color="#3a7fd0"/>
          <stop offset="0.45" stop-color="#2a6cc0"/>
          <stop offset="1" stop-color="#134689"/>
        </linearGradient>
      </defs>
      <path d="M0,306 C300,356 700,236 1050,208 L1050,600 L0,600 Z" fill="#d7262e"/>
      <path d="M0,322 C300,372 700,252 1050,224 L1050,600 L0,600 Z" fill="#ffffff"/>
      <path d="M0,334 C300,384 700,264 1050,236 L1050,600 L0,600 Z" fill="url(#blueBand)"/>
    </svg>

    <header class="brand">
      <div class="brand-dot"></div>
      <p class="brand-name">Quiet Harbor<br>Dental Urgent Clinic</p>
    </header>

    <div class="identity">
      <p class="person-name">Peter Delacroix, Jr., DMD</p>
      <p class="person-title">Founder/ CEO</p>
    </div>

    <address class="address">
      2718 Pellam Rd Ste 412<br>
      Houston, TX 77291
    </address>

    <div class="divider"></div>

    <ul class="contacts">
      <li>
        <span class="contact-icon">
          <svg viewBox="0 0 24 24"><path fill="#1f5fae" d="M6.6 10.8a15 15 0 0 0 6.6 6.6l2.2-2.2c.3-.3.7-.4 1-.2 1.1.4 2.3.6 3.6.6.6 0 1 .4 1 1V20c0 .6-.4 1-1 1A17 17 0 0 1 3 4c0-.6.4-1 1-1h3.5c.6 0 1 .4 1 1 0 1.3.2 2.5.6 3.6.1.3 0 .7-.2 1z"/></svg>
        </span>
        1-855-GRIN-WELLS
      </li>
      <li>
        <span class="contact-icon">
          <svg viewBox="0 0 24 24"><rect x="3" y="6" width="18" height="12" rx="1.5" fill="#1f5fae"/><path d="M3.5 7l8.5 6 8.5-6" stroke="#fff" stroke-width="1.6" fill="none"/></svg>
        </span>
        petedx4@mailvane.example
      </li>
      <li>
        <span class="contact-icon">
          <svg viewBox="0 0 24 24"><g fill="none" stroke="#1f5fae" stroke-width="2"><circle cx="12" cy="12" r="9"/><ellipse cx="12" cy="12" rx="4" ry="9"/><path d="M3 12h18"/></g></svg>
        </span>
        www.GRINWELLS.example
      </li>
    </ul>
  </section>
</main>
</body>
</html>
```